Business card for a plastic surgeon

i need a business card for a plastic surgeon. I have two adresses. The card should communicate safety, simmetry, beauty and with soft colors.
What i want in the card:
- my logo: Letters "R"and "B" (picture uploaded)
- my name: Renato Bastiani
- my registration: CRM 507 219
- my adresses and phone numbers (2):
- Av Dr Teixeira Lopes, 2710, sala 305 - Vila Olímpia | São Paulo/ SP - Phone: 11 4172-5036
- Al. Itapeva, 47, 3 andar - Alphaville | Barueri/ SP - Phone: 11 6350-2481

- my social network: site, facebook and instagram

Target Market(s)

people (95% girls and women) that want cosmetic procedures and plastic surgery

Industry/Entity Type

Business

Contact Information for Business Card

The card should communicate safety, simmetry, beauty and with soft colors.
Beige, brown, gray, rosy are some options. Color is free

Font styles to use
Serif

Requirements
Must have
• - my logo: Letters "R"and "B" (picture uploaded)
• - my name: Renato Bastiani
• - my registration: CRM 507 219
• - my adresses and phone numbers (2):
• - Av Dr Teixeira Lopes, 2710, sala 305 - Vila Olímpia | São Paulo/ SP - Phone: 11 4172-5036
• - Al. Itapeva, 47, 3 andar - Alphaville | Barueri/ SP - Phone: 11 6350-2481
• - my social network: site, facebook and instagram
Should not have
• other images (only my logo)

```html
<!DOCTYPE html>
<html lang="pt">
<head>
<meta charset="utf-8">
<title>Renato Bastiani – Cartão de Visita</title>
<link rel="stylesheet" href="https://fonts.googleapis.com/css2?family=Cinzel:wght@400;600;700&display=swap">
<style>
  :root{
    --amber:#fbb545;
    --ink:#0a0a0a;
    --paper:#e6e6e6;
    --cream:#fff3dc;
    --white:#f4f4f4;
  }
  *{margin:0;padding:0;box-sizing:border-box}
  html,body{width:1200px;height:900px;overflow:hidden;background:var(--paper)}
  body{font-family:"Cinzel",serif;position:relative}
  .card{position:absolute;left:250px;width:700px;height:389px;box-shadow:0 6px 18px rgba(0,0,0,.18)}
  .card--front{top:40px;background:var(--amber);color:var(--ink);display:flex;flex-direction:column;align-items:center;justify-content:center}
  .monogram{font-size:88px;font-weight:600;letter-spacing:4px;line-height:1;margin-bottom:26px}
  .front-name{font-size:34px;font-weight:400;letter-spacing:1px;line-height:1}
  .front-title{font-size:15px;letter-spacing:9px;margin-top:8px;padding-left:9px}

  .card--back{top:471px;background:var(--ink);overflow:hidden}
  .back-monogram{position:absolute;top:46px;right:58px;font-size:34px;font-weight:600;color:var(--amber);letter-spacing:2px}
  .social{position:absolute;right:40px;top:232px;display:flex;align-items:center;gap:7px;color:var(--white);font-size:11px;letter-spacing:1.5px}
  .social__mark{width:10px;height:10px;background:var(--amber)}
  .identity{position:absolute;left:50px;top:190px}
  .identity__name{color:var(--amber);font-size:28px;font-weight:600;letter-spacing:.5px;line-height:1}
  .identity__crm{color:var(--white);font-size:15px;letter-spacing:3px;margin-top:6px}
  .identity__contact{margin-top:24px;font-size:11px;letter-spacing:1.2px;line-height:1.35;color:var(--white)}
  .identity__phone{color:var(--amber)}
  .addresses{position:absolute;left:0;right:0;bottom:0;height:66px;background:var(--amber);color:var(--cream);display:flex;flex-direction:column;justify-content:center;align-items:center;font-size:11.5px;letter-spacing:1.2px;line-height:1.6}
</style>
</head>
<body>
  <section class="card card--front" aria-label="Frente do cartão">
    <div class="monogram">RB</div>
    <h1 class="front-name">DR. RENATO BASTIANI</h1>
    <p class="front-title">CIRURGIÃO PLÁSTICO</p>
  </section>

  <section class="card card--back" aria-label="Verso do cartão">
    <div class="back-monogram">RB</div>
    <div class="social"><span class="social__mark"></span>@RenatoBastiani</div>
    <div class="identity">
      <h2 class="identity__name">Renato Bastiani</h2>
      <p class="identity__crm">CRM 507 219</p>
      <div class="identity__contact">
        <p class="identity__phone">+55 11 3085 4420</p>
        <p>Moreira Garden Complex</p>
        <p>Lumen Park, Brasil 04538</p>
      </div>
    </div>
    <div class="addresses">
      <p>Av Dr Teixeira Lopes, 2710, sala 305 - Vila Olímpia | São Paulo/ SP - Phone: 11 4172-5036</p>
      <p>Al. Itapeva, 47, 3 andar - Alphaville | Barueri/ SP - Phone: 11 6350-2481</p>
    </div>
  </section>
</body>
</html>
```